Unique Elegant Stationary Set

Prepare a unique eye catching stationary set consisting of :
(1) Letterhead
(2) A3 Envelope
(3) Business Card
(4) Email Signature Banner

Package to be elegant, modern, and designers not only to think of design or colors but also materials could make a big difference, embossing, debossing, glossy, matt ....etc.

I attached both our new logos (Stacked or Linear) noting you may use any of them but you cant modify anything in the logos. Also attached our final draft portfolio to see what type of projects we work on and i also have here a glimboard page link showing the direction we want: https://www.glimboard.example/ravelkoton/business-card-design/

Target Market(s)

VVIP / Elite Developers

Industry/Entity Type

Architecture

Font styles to use
Sans Serif
Other font styles liked:
• unitext

Requirements
Should not have
• too many colors, or being busy in general. We want something pleasing to the eye

```html
<!DOCTYPE html>
<html lang="en">
<head>
<meta charset="utf-8">
<title>Vello Design — Business Card</title>
<link href="https://fonts.googleapis.com/css2?family=Lato:wght@300;400;700&display=swap" rel="stylesheet">
<style>
  :root {
    --backdrop: #b9b9b9;
    --backdrop-deep: #8f8f8f;
    --card: #2a2a2b;
    --card-edge: #1c1c1d;
    --deboss: #1d1d1e;
    --deboss-light: #3a3a3b;
    --ink: #f2f2f2;
    --ink-soft: #bdbdbd;
    --copper: #c07a3e;
  }
  * { margin: 0; padding: 0; box-sizing: border-box; }
  html, body { width: 1200px; height: 986px; overflow: hidden; }
  body {
    background: radial-gradient(ellipse at 40% 20%, #d2d1d1 0%, var(--backdrop) 45%, var(--backdrop-deep) 100%);
    font-family: "Lato", sans-serif;
    position: relative;
  }
  .card {
    position: absolute;
    width: 560px;
    height: 320px;
    background: var(--card);
    border-radius: 22px;
    box-shadow: 0 2px 0 var(--card-edge), 0 4px 0 #111, 0 6px 0 var(--card-edge), 0 8px 0 #111, 0 24px 40px rgba(0,0,0,.35);
  }
  .card--front { left: 80px; top: 110px; }
  .card--back { left: 560px; top: 540px; }

  /* Front: debossed wordmark */
  .front-brand {
    position: absolute;
    inset: 0;
    display: flex;
    flex-direction: column;
    align-items: center;
    justify-content: center;
    gap: 26px;
  }
  .front-brand__name {
    font-weight: 700;
    font-size: 52px;
    letter-spacing: 10px;
    color: var(--deboss);
    text-shadow: 0 1px 0 var(--deboss-light);
  }
  .front-brand__url {
    font-weight: 700;
    font-size: 15px;
    letter-spacing: .5px;
    color: var(--deboss);
    text-shadow: 0 1px 0 var(--deboss-light);
  }

  /* Back: contact side */
  .holder {
    position: absolute;
    left: 250px;
    top: 64px;
    color: var(--ink);
  }
  .holder__name { font-size: 20px; font-weight: 400; letter-spacing: .5px; }
  .holder__role { font-size: 12px; font-weight: 300; color: var(--ink-soft); letter-spacing: .5px; margin-top: 4px; }

  .contacts {
    position: absolute;
    left: 250px;
    top: 140px;
    list-style: none;
    color: var(--ink);
    font-size: 14px;
    line-height: 1;
  }
  .contacts li { display: flex; align-items: center; gap: 10px; margin-bottom: 9px; }
  .contacts svg { width: 18px; height: 18px; flex: none; }
  .contacts .address { display: block; padding-left: 28px; line-height: 1.4; margin-top: 4px; }

  .back-brand {
    position: absolute;
    left: 36px;
    bottom: 32px;
    font-weight: 700;
    font-size: 24px;
    line-height: 1.15;
    letter-spacing: 6px;
    color: var(--copper);
  }
</style>
</head>
<body>

<section class="card card--front" aria-label="Business card front">
  <div class="front-brand">
    <div class="front-brand__name">VELLO DESIGN</div>
    <div class="front-brand__url">WWW.VELLODESIGN.EXAMPLE</div>
  </div>
</section>

<section class="card card--back" aria-label="Business card back">
  <div class="holder">
    <div class="holder__name">SAMIR NAME</div>
    <div class="holder__role">DESIGNATION</div>
  </div>

  <ul class="contacts">
    <li>
      <svg viewBox="0 0 20 20" fill="none" stroke="#f2f2f2" stroke-width="1.3"><circle cx="10" cy="10" r="8.8"/><path d="M7 5.5l1.6 2.4-1 1.1c.6 1.3 1.5 2.2 2.8 2.8l1.1-1 2.4 1.6-.9 1.6c-3.4-.2-6.8-3.6-7-7z"/></svg>
      <span>+971 2 555 0142</span>
    </li>
    <li>
      <svg viewBox="0 0 20 20" fill="none" stroke="#f2f2f2" stroke-width="1.3"><circle cx="10" cy="10" r="8.8"/><rect x="5.5" y="7" width="9" height="6.5"/><path d="M5.5 7l4.5 3.5L14.5 7"/></svg>
      <span>INFO@VELLODESIGN.EXAMPLE</span>
    </li>
    <li>
      <svg viewBox="0 0 20 20" fill="none" stroke="#f2f2f2" stroke-width="1.3"><circle cx="10" cy="10" r="8.8"/><circle cx="10" cy="10" r="5"/><ellipse cx="10" cy="10" rx="2.2" ry="5"/><path d="M5 10h10"/></svg>
      <span>WWW.VELLODESIGN.EXAMPLE</span>
    </li>
    <li class="address">MERIDIAN TOWER, 14th FLOOR, 1408<br>P.O. BOX: 50219</li>
  </ul>

  <div class="back-brand">VELLO<br>DESIGN</div>
</section>

</body>
</html>
```